My business is primarily as a Herbalist, using Iridology to diagnose areas of weakness and which body systems need support and then dispensing a Herbal tonic. I also do Reflexology, Aromatherapy, Craniosacral Therapy, Reiki and make Organic Herbal Tea Blends.I don't have a logo. I will also be needing to update my business cards soon, but firstly need labels for a new product I've devised - CLEAR MIND BREW.This tea is powdered and is a combination of 16 herbs which help to nourish the brain tissues & support circulation to the brain, helping to prevent & prolong Dementia while also improving energy & vitality.My business colour is Magenta. My name is Delia Voskaridou, so maybe just use DELIA on the label.Please print address & mobile at the base of the label.81 Tulloch Rd Srathfield 2135 NSW | 0438172604 | The label needs to be round & no larger than 6cm

Target Market(s)

Universal

Industry/Entity Type

Health And Wellness

Font styles to use
Serif

Colors
6b449b
a64599

Requirements
Must have
• Magenta colour as a background.This colour is my so called trademark.
• DELIA- as a logo
• I want some vintage designs of florals with modern design.
• ORGANIC Herbal TEA blends
• CLEAR MIND BREW
• 200g
• Address & mobile at the base of label
Nice to have
• An improvement to my business card design & outlay.
• I love vintage but I also want it current. Sophisticated & stylish.
• It needs to represent quality & longevity & trust.

```html
<!DOCTYPE html>
<html lang="en">
<head>
<meta charset="utf-8">
<title>Clear Mind Brew – Tea Label</title>
<link href="https://fonts.googleapis.com/css2?family=Oswald:wght@300;400;500&display=swap" rel="stylesheet">
<style>
  :root {
    --page-bg: #f2efe9;
    --cream: #ebe5d5;
    --floral-light: #cfc7b5;
    --floral-deep: #a59d8e;
    --magenta: #a8388f;
    --plum: #5a0a42;
    --charcoal: #2f2d2e;
    --ink: #3a3536;
  }
  html, body {
    margin: 0;
    padding: 0;
    width: 1199px;
    height: 1200px;
    overflow: hidden;
    background: var(--page-bg);
  }
  .label-canvas {
    display: block;
    width: 1199px;
    height: 1200px;
  }
  .arc-title {
    font-family: 'Oswald', sans-serif;
    font-weight: 400;
    font-size: 34px;
    letter-spacing: 2px;
    fill: var(--cream);
  }
  .arc-contact {
    font-family: 'Oswald', sans-serif;
    font-weight: 300;
    font-size: 26px;
    fill: var(--cream);
  }
  .brand-name {
    font-family: 'Oswald', sans-serif;
    font-weight: 400;
    font-size: 50px;
    letter-spacing: 3px;
    fill: var(--magenta);
  }
  .product-name {
    font-family: 'Oswald', sans-serif;
    font-weight: 500;
    font-size: 66px;
    letter-spacing: 1px;
    fill: var(--cream);
  }
  .directions {
    font-family: 'Oswald', sans-serif;
    font-weight: 300;
    font-size: 19px;
    fill: var(--ink);
  }
  .net-weight {
    font-family: 'Oswald', sans-serif;
    font-weight: 400;
    font-size: 26px;
    fill: var(--ink);
  }
</style>
</head>
<body>
<svg class="label-canvas" viewBox="0 0 1199 1200" xmlns="http://www.w3.org/2000/svg">
  <defs>
    <radialGradient id="florals-tone" cx="50%" cy="50%" r="50%">
      <stop offset="72%" stop-color="var(--floral-deep)"/>
      <stop offset="100%" stop-color="var(--floral-light)"/>
    </radialGradient>
    <path id="top-arc" d="M 370 600 A 230 230 0 0 1 830 600"/>
    <path id="bottom-arc" d="M 349 600 A 251 251 0 0 0 851 600"/>
  </defs>

  <!-- label base -->
  <circle class="label-base" cx="600" cy="600" r="377" fill="var(--cream)"/>

  <!-- floral wreath area -->
  <path class="floral-wreath" role="img"
        aria-label="Vintage line-drawn wreath of herbs and flowers: roses, ginkgo leaves, rosemary, fennel and wildflowers"
        fill="url(#florals-tone)" fill-rule="evenodd"
        d="M 600 238 A 362 362 0 1 1 599.9 238 Z M 600 320 A 280 280 0 1 0 600.1 320 Z"/>

  <!-- scalloped seal -->
  <circle class="seal-edge" cx="600" cy="600" r="274" fill="none" stroke="var(--charcoal)"
          stroke-width="12" stroke-dasharray="0 14" stroke-linecap="round"/>
  <circle class="seal" cx="600" cy="600" r="272" fill="var(--charcoal)"/>
  <circle class="seal-ring" cx="600" cy="600" r="266" fill="var(--magenta)"/>
  <circle class="seal-rule" cx="600" cy="600" r="259" fill="none" stroke="var(--charcoal)" stroke-width="3"/>
  <circle class="seal-center" cx="600" cy="600" r="210" fill="var(--cream)"/>
  <circle class="seal-stitch" cx="600" cy="600" r="216" fill="none" stroke="var(--cream)"
          stroke-width="2" stroke-dasharray="3 5"/>

  <!-- curved headings -->
  <text class="arc-title" text-anchor="middle">
    <textPath href="#top-arc" startOffset="50%">ORGANIC HERBAL TEA BLENDS</textPath>
  </text>
  <text class="arc-contact" text-anchor="middle">
    <textPath href="#bottom-arc" startOffset="50%">81 Tulloch Rd Srathfield 2135 NSW • 0438172604</textPath>
  </text>

  <!-- brand -->
  <text class="brand-name" x="600" y="488" text-anchor="middle">DELIA</text>

  <!-- product band -->
  <rect class="product-band" x="332" y="514" width="536" height="94" fill="var(--plum)"/>
  <text class="product-name" x="600" y="588" text-anchor="middle">CLEAR MIND BREW</text>

  <!-- directions & weight -->
  <text class="directions" x="600" y="652" text-anchor="middle">Place 1/2 teaspoon in a mug.</text>
  <text class="directions" x="600" y="678" text-anchor="middle">Pour boiled water in and stir well.</text>
  <text class="net-weight" x="600" y="728" text-anchor="middle">• 200g•</text>
</svg>
</body>
</html>
```